Industrial design for commercialization of products for cargo

Good morning, we need a website design divided into 4 sections for a newly created company. Vextrano means Industrial Products for Loading and Pumping. We are located in the capital of Mexico and distributed throughout the country. We sell a wide range of equipment and accessories, for handling and lifting of load: hoists, traction devices, trolleys, pulleys, cables, shackles, tensioners, rings, marine chains, among others, as well as pneumatic double diaphragm pumps And centrifugal pumps, used in the pharmaceutical, chemical, food, etc. industries. Our products are manufactured to the highest quality standards, most are manufactured in the United States. Recently, Studio Flarn (ROLM.TAVEK) produced our company logo and we would like our website to be combined with it. We want the website to have an industrial design, that the colors combine with the logo and black letters. The images and information that we will use are in our current web page: www.vextrano.example. If you need more information, please let us know. My name is Lucia Fendrel and my email is ventasvextrano@mailzo.example. Thank you. PD Please, I want the winner to upload to my server, the coded files html and CSS through FTP (File Transfer Protocol) I know this action means an extra cost, but I m willing to pay. Thanks.
Target Market(s)
Our market is very broad, among our clients are companies in the construction industry, manufacturing, as well as department stores, warehouses, even shops, seaports.
Industry/Entity Type
Commercial
Coding
Coded - Design and coding required
Number of Pages Required
5+ page
Font styles to use
Other font styles liked:
- Hay libertad en cuanto a la tipografía, pueden utilizar la que ustedes consideren conveniente.

Colors
Designer to choose colors to be used in the design.
Requirements
Must have
- The page that we want should be divided into the sections that you consider convenient. SECTION OF HOME INFORMATION.- Our data, biography, mission, vision, values, company address, telephone number, whatsapp, email and location map. PRODUCTS FOR LOADING. PRODUCTS FOR PUMPING. ACCESSORIES FOR LOADING. CONTACT.

Nice to have
- One design you can use as an example is the page of one of our suppliers: www.tuvalde.example.mx, we would like our page to be better than that of this provider. We want you to have a better presentation. I would like them to use banners at the top and bottom where phone numbers are placed. I wish there was a space for the videos to run the products. My page must be in the Spanish language please. The choice of colors is at your discretion, however instead of the color orange, I would like them to use the color red.

Should not have
- My project should not seem unprofessional, but to show that we are a serious and important company. Do not look anything like our current page www.vextrano.example We do not want the option to add to the shopping cart or a page with a catalog. Our page is just a means to promote our products. Sales are done by phone.

```html
<!DOCTYPE html>
<html lang="en">
<head>
<meta charset="utf-8">
<title>Vextrano — Industrial Products for Loading and Pumping</title>
<link href="https://fonts.googleapis.com/css2?family=Roboto:wght@300;400;500;700&family=Roboto+Condensed:wght@400;700&display=swap" rel="stylesheet">
<style>
:root{
  --red:#c8321f;
  --red-dark:#8e1b1e;
  --orange:#d9542a;
  --ink:#222;
  --text:#666;
  --muted:#999;
  --light:#f2f2f2;
  --white:#fff;
}
*{box-sizing:border-box;margin:0;padding:0}
html,body{width:1200px;height:3636px;overflow:hidden}
body{font-family:"Roboto",Arial,sans-serif;color:var(--ink);background:var(--white);position:relative}
section,header,footer{position:absolute;left:0;width:1200px;overflow:hidden}
h2{font-family:"Roboto Condensed",Arial,sans-serif;font-weight:700}

/* header */
.site-header{top:0;height:128px;background:var(--white)}
.brand{position:absolute;left:28px;top:22px;display:flex;align-items:center;gap:12px}
.brand-mark{width:44px;height:44px;background:var(--red)}
.brand-name{font-family:"Roboto Condensed",sans-serif;font-weight:700;font-size:36px;color:var(--ink);letter-spacing:1px}
.brand-tag{position:absolute;left:28px;top:76px;font-size:10px;color:var(--muted);letter-spacing:.5px}
.contact{position:absolute;top:10px;display:flex;gap:8px;font-size:12px}
.contact svg{margin-top:2px;flex:none}
.contact b{display:block;font-size:10px;color:var(--ink);font-weight:500}
.contact span{color:var(--red);font-weight:500}
.nav{position:absolute;right:110px;top:76px;display:flex;gap:26px;font-size:13px;font-weight:500;letter-spacing:.3px}
.nav a{color:var(--ink);text-decoration:none}
.nav a.active{color:var(--red)}

/* hero */
.hero{top:128px;height:572px;background:
  radial-gradient(ellipse 300px 260px at 88% 62%,rgba(214,184,48,.85),rgba(214,184,48,0) 70%),
  radial-gradient(ellipse 260px 320px at 32% 55%,rgba(38,70,110,.8),rgba(38,70,110,0) 70%),
  linear-gradient(110deg,#3a4650 0%,#68788a 35%,#8c969c 60%,#a9a38e 85%,#4a5158 100%)}
.hero-copy{position:absolute;top:198px;width:100%;text-align:center;color:var(--white)}
.hero-copy h1{font-family:"Roboto Condensed",sans-serif;font-size:38px;font-weight:700;letter-spacing:1px}
.hero-copy p{font-size:28px;font-weight:400;margin-top:4px}
.btn-outline{display:inline-block;border:1px solid currentColor;font-size:12px;font-weight:500;padding:9px 18px;letter-spacing:.5px}
.hero-copy .btn-outline{margin-top:22px}
.dots{position:absolute;bottom:18px;width:100%;display:flex;justify-content:center;gap:8px}
.dots i{width:9px;height:9px;border-radius:50%;background:rgba(255,255,255,.5)}
.dots i.on{background:var(--white)}

/* welcome */
.welcome{top:700px;height:480px;background:var(--white)}
.welcome-copy{position:absolute;left:120px;top:100px;width:440px}
.welcome-copy h2{font-size:30px;color:var(--ink)}
.welcome-copy p{font-size:12px;line-height:1.7;color:var(--text);margin-top:18px}
.welcome-copy .btn-outline{margin-top:24px;color:var(--red)}
.welcome-photo{position:absolute;right:0;top:0;width:600px;height:480px;background:
  radial-gradient(ellipse 200px 120px at 55% 78%,rgba(40,100,190,.9),rgba(40,100,190,0) 75%),
  linear-gradient(135deg,#d4d8dc,#a7b0b8 45%,#7d8a96 75%,#5a6670);clip-path:polygon(90px 0,100% 0,100% 100%,0 100%)}
.welcome-edge{position:absolute;right:0;top:0;width:600px;height:480px}

/* why */
.why{top:1180px;height:460px;background:linear-gradient(180deg,var(--orange),var(--red));color:var(--white);text-align:center}
.why h2{font-size:28px;margin-top:50px}
.why p.lead{font-size:13px;width:640px;margin:12px auto 0;line-height:1.6;opacity:.9}
.features{display:flex;justify-content:center;gap:80px;margin-top:34px}
.feature{width:200px;height:200px;border:2px solid var(--white);border-radius:50%;display:flex;flex-direction:column;align-items:center;justify-content:center;gap:12px;font-weight:700;font-size:15px;line-height:1.2}

/* products */
.products{top:1640px;height:510px;background:var(--white);text-align:center}
.products h2{font-size:26px;margin-top:48px}
.product-row{position:absolute;top:130px;left:150px;width:900px;display:flex;justify-content:space-between}
.product{width:190px}
.product-img{height:130px}
.product h3{font-size:17px;color:var(--red);font-weight:500;margin-top:18px}
.product p{font-size:10.5px;color:var(--muted);line-height:1.6;margin-top:8px}
.btn-dark{display:inline-block;background:#3a3a3a;color:var(--white);font-size:9.5px;font-weight:700;padding:7px 14px;margin-top:14px}
.arrow{position:absolute;top:205px}

/* testimonials */
.testimonials{top:2150px;height:440px;background:
  radial-gradient(ellipse 220px 200px at 78% 40%,rgba(210,220,226,.6),rgba(210,220,226,0) 70%),
  linear-gradient(120deg,#b8c0c4,#6f7e88 45%,#2f4250)}
.testi-band{position:absolute;left:0;top:0;width:720px;height:440px;background:linear-gradient(135deg,#a52127,var(--red-dark));clip-path:polygon(0 0,100% 0,78% 100%,0 100%)}
.testi-copy{position:absolute;left:110px;top:40px;width:420px;color:var(--white);text-align:center}
.testi-copy h2{font-size:24px;text-align:left;margin-left:40px}
.avatar{width:70px;height:70px;border-radius:50%;background:#c9a488;margin:22px auto 0;border:2px solid var(--white)}
.quote{font-size:12.5px;line-height:1.7;margin-top:20px;position:relative;padding:0 30px}
.quote:before,.quote:after{font-family:Georgia,serif;font-size:48px;position:absolute;line-height:1}
.quote:before{content:"\201C";left:0;top:-6px}
.quote:after{content:"\201D";right:0;bottom:-26px}
.author{font-size:13px;margin-top:20px}
.testi-dots{display:flex;justify-content:center;gap:7px;margin-top:14px}
.testi-dots i{width:8px;height:8px;border-radius:50%;background:rgba(255,255,255,.5)}
.testi-dots i.on{background:var(--white)}

/* brands */
.brands{top:2590px;height:280px;background:var(--light);text-align:center}
.brands h2{font-size:22px;color:#444;margin-top:80px}
.brand-row{display:flex;justify-content:center;gap:70px;margin-top:50px;color:#7a7a7a;font-size:22px}
.brand-row span:nth-child(1){font-family:"Roboto Condensed",sans-serif;font-weight:700}
.brand-row span:nth-child(3){letter-spacing:2px;font-weight:500}
.brand-row span:nth-child(6){font-family:"Roboto Condensed",sans-serif;font-weight:700;letter-spacing:1px}

/* blogs */
.blogs{top:2870px;height:330px;background:linear-gradient(180deg,#dcdcdc,#cfcfcf)}
.blogs h2{position:absolute;left:120px;top:44px;font-size:22px;color:#333}
.blog{position:absolute;top:110px;width:430px;display:flex;gap:18px}
.blog-img{width:190px;height:115px;flex:none}
.blog h3{font-size:15px;color:var(--red);font-weight:500}
.blog p{font-size:10.5px;color:var(--text);line-height:1.6;margin-top:8px}
.blog a{display:inline-block;font-size:10px;color:var(--red);margin-top:8px;text-decoration:none;font-weight:500}

/* footer */
.site-footer{top:3200px;height:400px;background:linear-gradient(180deg,#f4f4f4,#ececec)}
.footer-brand{position:absolute;left:120px;top:62px;display:flex;align-items:center;gap:12px}
.footer-tag{position:absolute;left:120px;top:118px;font-size:10px;color:var(--muted)}
.footer-col{position:absolute;top:60px}
.footer-col h4{font-size:14px;color:var(--red);font-weight:700;letter-spacing:.5px}
.footer-col ul{list-style:none;margin-top:12px}
.footer-col li{font-size:12px;color:var(--text);line-height:1.9}
.social{display:flex;gap:8px;margin-top:14px}
.social i{width:30px;height:30px;border-radius:50%;background:#555}
.copyright{position:absolute;left:0;top:3600px;width:1200px;height:36px;background:#e0e0e0;font-size:10px;color:var(--muted);text-align:center;line-height:36px}
</style>
</head>
<body>

<header class="site-header">
  <div class="brand"><div class="brand-mark"></div><div class="brand-name">VEXTRANO</div></div>
  <div class="brand-tag">PRODUCTOS INDUSTRIALES PARA CARGA Y BOMBEO</div>

  <div class="contact" style="left:560px">
    <svg width="16" height="16" viewBox="0 0 24 24" fill="#c8321f"><path d="M6.6 10.8a15 15 0 0 0 6.6 6.6l2.2-2.2a1 1 0 0 1 1-.25 11 11 0 0 0 3.6.6 1 1 0 0 1 1 1V20a1 1 0 0 1-1 1A17 17 0 0 1 3 4a1 1 0 0 1 1-1h3.5a1 1 0 0 1 1 1 11 11 0 0 0 .6 3.6 1 1 0 0 1-.25 1z"/></svg>
    <div><b>CALL:</b><span>01 55 4120 3398</span></div>
  </div>
  <div class="contact" style="left:720px">
    <svg width="16" height="16" viewBox="0 0 24 24" fill="none" stroke="#c8321f" stroke-width="2"><circle cx="12" cy="12" r="9"/><path d="M8.5 10.5c1 2.5 2.5 4 5 5l1.5-1.5"/></svg>
    <div><b>WHATSAPP:</b><span>01 5870 2261</span></div>
  </div>
  <div class="contact" style="left:880px">
    <svg width="16" height="16" viewBox="0 0 24 24" fill="none" stroke="#c8321f" stroke-width="2"><rect x="3" y="5" width="18" height="14"/><path d="M3 6l9 7 9-7"/></svg>
    <div><b>EMAIL:</b><span style="font-size:10px">ventasvextrano@mailzo.example</span><br><span style="font-size:10px">info@vextrano.example</span></div>
  </div>

  <nav class="nav">
    <a class="active">HOME</a><a>INFORMATION</a><a>LOADING</a><a>PUMPING</a><a>ACCESSORIES</a><a>CONTACT US</a>
  </nav>
</header>

<section class="hero" role="img" aria-label="Photo: technician in a yellow hard hat working beside an industrial hoist and a yellow cable drum">
  <div class="hero-copy">
    <h1>WE SELL A WIDE RANGE OF EQUIPMENT</h1>
    <p>&amp; ACCESSORIES, FOR HANDLING AND LIFTING</p>
    <span class="btn-outline">SHOP NOW</span>
  </div>
  <div class="dots"><i class="on"></i><i></i><i></i><i></i></div>
</section>

<section class="welcome">
  <div class="welcome-copy">
    <h2>WELCOME TO OUR WEBSITE</h2>
    <p>Vextrano distributes industrial loading and pumping equipment across the country from our base in Mexico City, backed by trusted manufacturers and expert service.</p>
    <p>Our catalogue covers hoists, trolleys, pulleys, shackles, chains and diaphragm pumps built to the highest quality standards for demanding industries.</p>
    <span class="btn-outline">READ MORE</span>
  </div>
  <div class="welcome-photo" role="img" aria-label="Photo: blue centrifugal pumps connected to steel pipework in a plant room"></div>
  <svg class="welcome-edge" viewBox="0 0 600 480"><polygon points="60,0 96,0 6,480 0,480 0,320" fill="#c8321f"/></svg>
</section>

<section class="why">
  <h2>WHY CHOOSE US</h2>
  <p class="lead">We combine certified products, fast nationwide delivery and technical advice so every lifting and pumping job runs safely and on schedule for our clients.</p>
  <div class="features">
    <div class="feature">QUALITY<br>PRODUCT
      <svg width="54" height="54" viewBox="0 0 54 54" fill="none" stroke="#fff" stroke-width="2.5"><circle cx="27" cy="27" r="22"/><path d="M17 28l7 7 13-15"/></svg>
    </div>
    <div class="feature">OUR<br>ACCESSORIES
      <svg width="54" height="54" viewBox="0 0 54 54" fill="none" stroke="#fff" stroke-width="2.5"><circle cx="27" cy="27" r="10"/><circle cx="27" cy="27" r="20" stroke-dasharray="6 5"/></svg>
    </div>
    <div class="feature">OUR<br>SUPPORT
      <svg width="54" height="54" viewBox="0 0 54 54" fill="none" stroke="#fff" stroke-width="2.5"><rect x="8" y="10" width="38" height="26" rx="3"/><path d="M18 36l-4 10 12-10"/><path d="M16 20h22M16 27h14"/></svg>
    </div>
  </div>
</section>

<section class="products">
  <h2>OUR PRODUCTS</h2>
  <svg class="arrow" style="left:100px" width="16" height="30" viewBox="0 0 16 30"><path d="M14 2L2 15l12 13" fill="none" stroke="#999" stroke-width="2"/></svg>
  <svg class="arrow" style="right:100px" width="16" height="30" viewBox="0 0 16 30"><path d="M2 2l12 13L2 28" fill="none" stroke="#999" stroke-width="2"/></svg>
  <div class="product-row">
    <div class="product">
      <div class="product-img" role="img" aria-label="Photo: yellow electric chain hoist" style="background:radial-gradient(ellipse 70px 40px at 50% 45%,#e8cc30,#fff 100%)"></div>
      <h3>Product Name</h3>
      <p>Heavy duty unit rated for daily lifting work in plants, warehouses and busy loading docks nationwide.</p>
      <span class="btn-dark">READ MORE</span>
    </div>
    <div class="product">
      <div class="product-img" role="img" aria-label="Photo: red pulley blocks with steel hooks" style="background:radial-gradient(ellipse 60px 50px at 50% 45%,#b8352e,#fff 100%)"></div>
      <h3>Product Name</h3>
      <p>Forged steel blocks with sealed bearings that keep cable runs smooth under changing heavy loads.</p>
      <span class="btn-dark">READ MORE</span>
    </div>
    <div class="product">
      <div class="product-img" role="img" aria-label="Photo: black and silver cable puller with hook" style="background:radial-gradient(ellipse 70px 40px at 50% 50%,#4a4a4a,#fff 100%)"></div>
      <h3>Product Name</h3>
      <p>Manual traction device for pulling, tensioning and positioning loads where no power is available.</p>
      <span class="btn-dark">READ MORE</span>
    </div>
    <div class="product">
      <div class="product-img" role="img" aria-label="Photo: grey industrial electric motor" style="background:radial-gradient(ellipse 70px 45px at 50% 50%,#80868b,#fff 100%)"></div>
      <h3>Product Name</h3>
      <p>Reliable motor unit for centrifugal pumps used in chemical, food and pharmaceutical process lines.</p>
      <span class="btn-dark">READ MORE</span>
    </div>
  </div>
</section>

<section class="testimonials" role="img" aria-label="Photo: workers in a factory hall with steel structures and machinery">
  <div class="testi-band"></div>
  <div class="testi-copy">
    <h2>TESTIMONIALS</h2>
    <div class="avatar" role="img" aria-label="Client portrait"></div>
    <p class="quote">Their team helped us choose the right hoists and chains for our port operation, and every order arrived complete, certified and right on time.</p>
    <p class="author">By Author Name</p>
    <div class="testi-dots"><i class="on"></i><i></i><i></i></div>
  </div>
</section>

<section class="brands">
  <h2>OUR BRANDS</h2>
  <div class="brand-row">
    <span>KORVEN</span><span>Altemo</span><span>BRASSLINE</span><span>Nuvaro</span><span>tellix</span><span>DUNMARK</span>
  </div>
</section>

<section class="blogs">
  <h2>LATEST BLOGS</h2>
  <article class="blog" style="left:120px">
    <div class="blog-img" role="img" aria-label="Photo: welder working with sparks in a workshop" style="background:radial-gradient(ellipse 60px 40px at 60% 55%,#f0a040,#2c3440 100%)"></div>
    <div>
      <h3>Ullamcorper sed eget</h3>
      <p>How to inspect lifting chains and shackles before every shift, and the simple checks that extend equipment life and keep crews safe on site.</p>
      <a>READ MORE</a>
    </div>
  </article>
  <article class="blog" style="left:640px">
    <div class="blog-img" role="img" aria-label="Photo: industrial plant with chimneys under a blue sky" style="background:linear-gradient(180deg,#8fb3d9,#c9b38a 60%,#6d6a63)"></div>
    <div>
      <h3>Donec dictum lectus</h3>
      <p>Choosing between diaphragm and centrifugal pumps for your process line, with key points on flow, viscosity, materials and daily maintenance.</p>
      <a>READ MORE</a>
    </div>
  </article>
</section>

<footer class="site-footer">
  <div class="footer-brand"><div class="brand-mark"></div><div class="brand-name">VEXTRANO</div></div>
  <div class="footer-tag">PRODUCTOS INDUSTRIALES PARA CARGA Y BOMBEO</div>
  <div class="footer-col" style="left:600px">
    <h4>COMPANY</h4>
    <ul><li>Home</li><li>Information</li><li>Loading</li><li>Pumping</li></ul>
  </div>
  <div class="footer-col" style="left:780px">
    <h4>RESOURCES</h4>
    <ul><li>News</li><li>Blogs</li><li>Accessories</li><li>Contact us</li></ul>
  </div>
  <div class="footer-col" style="left:960px">
    <h4>STAY IN TOUCH</h4>
    <div class="social"><i></i><i></i><i></i><i></i></div>
  </div>
</footer>
<div class="copyright">© 2017 Vextrano. All rights reserved. Terms of Use.</div>

</body>
</html>
```